The K7 Momentum Collective Website

We have a pitch deck and messaging drafted. Target audience is academic institutions and VC investors that have seed money in start ups.

Need a basic website

Industry/Entity Type

LIfe Science, Diagnostic, medical device.

Coding

Coded - Design and coding required

Number of Pages Required

5+ page

```html
<!DOCTYPE html>
<html lang="en">
<head>
<meta charset="utf-8">
<title>The K7 Momentum Collective – Home Page Concepts</title>
<link href="https://fonts.googleapis.com/css2?family=Poppins:wght@400;500;600;700&family=Open+Sans:wght@400;600&display=swap" rel="stylesheet">
<style>
:root{
  --ink:#1d2433;
  --muted:#5d6575;
  --line:#dfe4ea;
  --teal:#1ba6cf;
  --navy:#0f2740;
  --navy-2:#16344f;
  --ice:#e8f4f9;
  --violet:#5b2ee8;
  --violet-2:#7a3cf2;
  --indigo:#3a2bd0;
  --lilac:#efeafe;
  --photo-a:#8f9aa8;
  --photo-b:#3d4a5c;
}
*{box-sizing:border-box;margin:0;padding:0}
html,body{width:1200px;height:3332px;overflow:hidden;background:#fff}
body{font-family:"Open Sans",Arial,sans-serif;color:var(--ink);position:relative}
h1,h2,h3,h4,.label,.logo,.btn{font-family:"Poppins",Arial,sans-serif}

.concept-title{position:absolute;top:28px;width:544px;text-align:center;font:500 26px "Poppins",Arial,sans-serif;color:#222}
.concept-title.v1{left:48px}.concept-title.v2{left:612px}

.page{position:absolute;top:80px;width:544px;height:3200px;background:#fff;box-shadow:0 2px 10px rgba(0,0,0,.12);overflow:hidden}
.page.v1{left:48px;--accent:var(--teal);--deep:var(--navy);--soft:var(--ice)}
.page.v2{left:612px;--accent:var(--violet);--deep:var(--indigo);--soft:var(--lilac)}

.photo{background:linear-gradient(135deg,var(--photo-a),var(--photo-b))}
.v2 .photo{background:linear-gradient(135deg,#9aa3c4,#3d3f78)}
.hex{clip-path:polygon(25% 3%,75% 3%,100% 50%,75% 97%,25% 97%,0 50%)}
.p{font-size:8.5px;line-height:1.6;color:var(--muted)}
.label{font-size:8px;font-weight:600;color:var(--accent);text-transform:uppercase;letter-spacing:.5px}
.btn{display:inline-block;background:var(--accent);color:#fff;font-size:8px;font-weight:600;padding:6px 14px;border-radius:3px}
.v2 .btn{border-radius:14px}
.sec-title{font-size:19px;font-weight:700;color:var(--ink);text-align:center}

/* header */
.hero{position:relative;height:300px;color:#fff}
.v1 .hero{background:linear-gradient(90deg,rgba(15,39,64,.92),rgba(15,39,64,.35)),linear-gradient(135deg,#a6b0bc,#46546a)}
.v2 .hero{background:linear-gradient(120deg,#4b28e0,#7a3cf2 60%,#5a48f0)}
.topbar{display:flex;justify-content:space-between;align-items:center;padding:8px 22px;height:36px}
.v1 .topbar{background:#fff;color:var(--ink)}
.logo{font-size:11px;font-weight:600}
.phone{font-size:8px;font-weight:600;border:1px solid currentColor;padding:4px 8px;border-radius:3px}
.menu{display:flex;gap:16px;padding:7px 22px;font-size:7.5px}
.v1 .menu{background:var(--navy)}
.v2 .menu{border-bottom:1px solid rgba(255,255,255,.2)}
.hero-copy{position:absolute;left:22px;top:112px;width:240px}
.hero-copy h1{font-size:24px;line-height:1.2;font-weight:700;margin-bottom:8px}
.hero-copy p{font-size:8.5px;line-height:1.6;opacity:.9;margin-bottom:14px}
.hero-art{position:absolute;right:22px;top:82px;width:230px;height:190px;border-radius:6px;background:linear-gradient(135deg,#8fe0e8,#3f8ff0 50%,#a86bff)}

/* about */
.about{height:240px;display:flex;align-items:center;padding:0 30px;gap:24px}
.about .txt{flex:1}
.about h2{font-size:19px;font-weight:700;margin:4px 0 10px}
.about .p{margin-bottom:12px}
.about .img{width:180px;height:160px}

/* solution */
.solution{height:280px;background:var(--soft);display:flex;align-items:center;padding:0 30px;gap:26px}
.v2 .solution{background:#fff}
.solution .img{width:190px;height:170px;flex:none}
.solution h2{font-size:19px;font-weight:700;margin:4px 0 8px}
.ticks{list-style:none;margin-top:8px}
.ticks li{font-size:8px;color:var(--muted);padding-left:14px;position:relative;margin-bottom:5px;line-height:1.5}
.ticks li::before{content:"";position:absolute;left:0;top:3px;width:7px;height:4px;border-left:2px solid var(--accent);border-bottom:2px solid var(--accent);transform:rotate(-45deg)}

/* discovery */
.discovery{height:220px;padding-top:34px}
.discovery svg{display:block;margin:22px auto 0}

/* product definition */
.product{height:1020px;position:relative;padding-top:30px}
.v2 .product::before{content:"";position:absolute;left:0;top:0;width:100%;height:180px;background:linear-gradient(120deg,#4b28e0,#7a3cf2);clip-path:polygon(0 0,100% 0,100% 55%,0 100%)}
.v2 .product .sec-title{color:#fff;position:relative}
.v2 .product .label.center{color:#e5dcff;position:relative}
.label.center{text-align:center;display:block;margin-bottom:4px}
.phase{position:relative;height:235px;display:flex;align-items:center;padding:0 30px;gap:30px}
.phase.flip{flex-direction:row-reverse}
.phase .txt{flex:1}
.phase h3{font-size:12px;font-weight:600;margin:3px 0 8px}
.phase .img{width:200px;height:180px;flex:none}
.v2 .phase.band{background:linear-gradient(120deg,#4b28e0,#7a3cf2)}
.v2 .phase.band h3,.v2 .phase.band .p{color:#fff}
.v2 .phase.band .label{color:#d9ceff}
.cols{display:grid;grid-template-columns:1fr 1fr;gap:4px 14px;margin-top:6px}
.cols span{font-size:7.5px;color:var(--muted);padding-left:9px;position:relative}
.cols span::before{content:"";position:absolute;left:0;top:4px;width:4px;height:4px;border-radius:50%;background:var(--accent)}

/* plan elements */
.plan{height:370px;padding-top:34px}
.v2 .plan{background:var(--soft)}
.grid{display:grid;grid-template-columns:repeat(3,1fr);gap:14px;padding:24px 34px 0}
.card{text-align:center;padding:14px 10px;height:130px}
.card .ico{display:block;margin:0 auto 8px}
.card h4{font-size:9.5px;font-weight:600;margin-bottom:6px}
.card .p{font-size:7.5px}
.card.on{background:var(--accent);color:#fff}
.card.on .p{color:#e8f6fb}
.v2 .card.on{background:linear-gradient(160deg,#7a3cf2,#4b28e0)}

/* key areas */
.areas{height:290px;display:flex;align-items:stretch}
.v2 .areas{background:linear-gradient(120deg,#4b28e0,#7a3cf2)}
.areas .txt{flex:1;padding:36px 18px 0 30px}
.areas h2{font-size:19px;font-weight:700;margin:4px 0 12px}
.v2 .areas h2{color:#fff}.v2 .areas .label{color:#d9ceff}
.table{display:grid;grid-template-columns:1fr 1fr;column-gap:12px}
.table div{font-size:7.5px;color:var(--muted);padding:5px 0;border-bottom:1px solid var(--line)}
.table b{color:var(--ink);font-weight:600}
.v2 .table div{color:#e5dcff;border-color:rgba(255,255,255,.25)}
.v2 .table b{color:#fff}
.areas .img{width:200px}

/* funding */
.funding{height:250px;padding-top:26px}
.funding .row{display:flex;align-items:center;gap:30px;padding:18px 30px 0}
.funding .img{width:190px;height:160px;border-radius:50%;flex:none}
.v1 .funding .img{border-radius:50%/50%;clip-path:ellipse(50% 50%)}
.lists{display:flex;gap:26px}
.lists h4{font-size:10px;font-weight:600;margin-bottom:8px}
.lists li{list-style:none;font-size:8px;color:var(--muted);margin-bottom:5px}

/* footer */
.foot{height:230px;position:relative}
.subscribe{height:44px;background:var(--teal);display:flex;align-items:center;justify-content:space-between;padding:0 30px;color:#fff}
.subscribe h4{font-size:11px;font-weight:600}
.field{display:flex}
.field span{width:140px;height:22px;background:#fff;font-size:7px;color:#999;padding:6px 8px}
.field b{background:var(--navy);font:600 7px "Poppins",Arial,sans-serif;padding:7px 10px}
.links{display:flex;gap:22px;padding:24px 30px;color:#cfd8e3}
.v1 .links{background:var(--navy);height:186px}
.v2 .foot{background:linear-gradient(120deg,#4b28e0,#7a3cf2)}
.v2 .links{padding-top:34px;height:196px}
.links .col{flex:1}
.links .logo{color:#fff;margin-bottom:8px}
.links h4{font-size:9px;color:#fff;margin-bottom:8px;font-weight:600}
.links li{list-style:none;font-size:7.5px;margin-bottom:5px}
.links p{font-size:7.5px;line-height:1.6}
.copy{position:absolute;left:0;bottom:0;width:100%;padding:8px 30px;font-size:7px;color:#a9b5c4;border-top:1px solid rgba(255,255,255,.15)}
</style>
</head>
<body>

<div class="concept-title v1">Home Page V. 01</div>
<div class="concept-title v2">Home Page V. 02</div>

<!-- ===== Version 1 ===== -->
<div class="page v1">
  <header class="hero">
    <div class="topbar"><span class="logo">The K7 Momentum Collective</span><span class="phone">(555) 014-2280</span></div>
    <nav class="menu"><span>Home</span><span>About Us</span><span>The Solution</span><span>Product Definition</span><span>Plan Elements</span><span>Funding</span><span>Contact</span></nav>
    <div class="hero-copy">
      <h1>The K7 Momentum Collective</h1>
      <p>Accelerating new life science ventures from discovery to market.</p>
      <span class="btn">Learn More</span>
    </div>
  </header>

  <section class="about">
    <div class="txt">
      <span class="label">About Us</span>
      <h2>The K7 Momentum Collective</h2>
      <p class="p">The K7 Momentum Collective guides academic inventors and early investors through a structured path that turns promising research in diagnostics and medical devices into a fundable company.</p>
      <span class="btn">Read More</span>
    </div>
    <div class="img photo hex" role="img" aria-label="Photo of a business professional in a suit"></div>
  </section>

  <section class="solution">
    <div class="img photo hex" role="img" aria-label="Photo of colleagues meeting around a table"></div>
    <div class="txt">
      <span class="label">What We Offer</span>
      <h2>The Solution</h2>
      <p class="p">A proven framework that reduces risk and shortens the time to a credible investment case.</p>
      <ul class="ticks">
        <li>Define the market and the clinical need</li>
        <li>Shape the product that wins the market</li>
        <li>Build the blueprint for development and launch</li>
        <li>Present a clear plan to investors and boards</li>
      </ul>
    </div>
  </section>

  <section class="discovery">
    <h2 class="sec-title">Discovery to Market</h2>
    <svg width="480" height="110" viewBox="0 0 480 110" aria-label="Five stage process from discovery to market">
      <g fill="none" stroke="#1ba6cf" stroke-width="2">
        <circle cx="48" cy="55" r="38"/><circle cx="144" cy="55" r="38"/><circle cx="240" cy="55" r="38"/><circle cx="336" cy="55" r="38"/><circle cx="432" cy="55" r="38"/>
      </g>
      <g stroke="#0f2740" stroke-width="1.5" fill="#0f2740">
        <line x1="86" y1="55" x2="104" y2="55"/><path d="M104 51 L110 55 L104 59Z"/>
        <line x1="182" y1="55" x2="200" y2="55"/><path d="M200 51 L206 55 L200 59Z"/>
        <line x1="278" y1="55" x2="296" y2="55"/><path d="M296 51 L302 55 L296 59Z"/>
        <line x1="374" y1="55" x2="392" y2="55"/><path d="M392 51 L398 55 L392 59Z"/>
      </g>
      <g font-family="Poppins,Arial,sans-serif" font-size="8" font-weight="600" fill="#1d2433" text-anchor="middle">
        <text x="48" y="58">Discovery</text>
        <text x="144" y="54">Market</text><text x="144" y="64">Case</text>
        <text x="240" y="54">Winning</text><text x="240" y="64">Product</text>
        <text x="336" y="54">Product</text><text x="336" y="64">Blueprint</text>
        <text x="432" y="54">Launch &amp;</text><text x="432" y="64">Funding</text>
      </g>
    </svg>
  </section>

  <section class="product">
    <span class="label center">Our Process</span>
    <h2 class="sec-title">Product Definition</h2>
    <div class="phase">
      <div class="txt"><span class="label">Phase 1</span><h3>The Market Case (30 – 45 days)</h3>
        <p class="p">We size the opportunity, map the competition and confirm the unmet clinical need. Interviews with clinicians, payers and buyers show who will pay and why the product matters.</p></div>
      <div class="img photo hex" role="img" aria-label="Photo of a city skyline with rising bar chart overlay"></div>
    </div>
    <div class="phase flip">
      <div class="txt"><span class="label">Phase 2</span><h3>The Winning Product (30 – 45 days)</h3>
        <p class="p">We turn market insight into product requirements, pricing and positioning, so the team builds what customers will adopt and investors will back.</p></div>
      <div class="img photo hex" role="img" aria-label="Photo of a professional pointing at a digital screen"></div>
    </div>
    <div class="phase">
      <div class="txt"><span class="label">Phase 3</span><h3>The Product Blueprint (45 – 60 days)</h3>
        <p class="p">A development roadmap with regulatory path, milestones, budget and team plan that carries the product from prototype to first sales.</p></div>
      <div class="img photo hex" role="img" aria-label="Photo of a team reviewing plans at a desk"></div>
    </div>
    <div class="phase flip">
      <div class="txt"><span class="label">Phase 4</span><h3>CEO Report out (15 days)</h3>
        <div class="cols"><span>Market summary</span><span>Product profile</span><span>Regulatory path</span><span>Funding needs</span><span>Key milestones</span><span>Risk review</span></div></div>
      <div class="img photo hex" role="img" aria-label="Photo of hands shaking over a business desk"></div>
    </div>
  </section>

  <section class="plan">
    <h2 class="sec-title">K7 Plan Elements</h2>
    <div class="grid">
      <div class="card"><svg class="ico" width="26" height="26"><circle cx="13" cy="13" r="11" fill="none" stroke="#1ba6cf" stroke-width="2"/></svg><h4>Executive Summary</h4><p class="p">A short view of the need, the product and the ask.</p></div>
      <div class="card on"><svg class="ico" width="26" height="26"><circle cx="13" cy="13" r="11" fill="none" stroke="#fff" stroke-width="2"/></svg><h4>Company Description</h4><p class="p">Mission, team, structure and the science behind it.</p></div>
      <div class="card"><svg class="ico" width="26" height="26"><circle cx="13" cy="13" r="11" fill="none" stroke="#1ba6cf" stroke-width="2"/></svg><h4>Products/Services</h4><p class="p">What we sell, who uses it and how it is priced.</p></div>
      <div class="card"><svg class="ico" width="26" height="26"><circle cx="13" cy="13" r="11" fill="none" stroke="#1ba6cf" stroke-width="2"/></svg><h4>Market Analysis</h4><p class="p">Size, segments, trends and the competitive field.</p></div>
      <div class="card"><svg class="ico" width="26" height="26"><circle cx="13" cy="13" r="11" fill="none" stroke="#1ba6cf" stroke-width="2"/></svg><h4>Operational Strategy</h4><p class="p">Development, quality, supply and go to market.</p></div>
      <div class="card"><svg class="ico" width="26" height="26"><circle cx="13" cy="13" r="11" fill="none" stroke="#1ba6cf" stroke-width="2"/></svg><h4>Financials</h4><p class="p">Forecasts, budget and the use of funds raised.</p></div>
    </div>
  </section>

  <section class="areas">
    <div class="txt">
      <span class="label">What We Cover</span>
      <h2>Key areas Covered</h2>
      <div class="table">
        <div><b>Clinical need</b> and use</div><div><b>Pricing</b> model</div>
        <div><b>Market size</b> and growth</div><div><b>Reimbursement</b> path</div>
        <div><b>Competition</b> review</div><div><b>Regulatory</b> plan</div>
        <div><b>Customer</b> interviews</div><div><b>IP</b> position</div>
        <div><b>Product</b> requirements</div><div><b>Team</b> and hiring</div>
        <div><b>Positioning</b> and message</div><div><b>Funding</b> strategy</div>
      </div>
    </div>
    <div class="img photo" role="img" aria-label="Photo of a smiling businessman in a suit"></div>
  </section>

  <section class="funding">
    <h2 class="sec-title">Funding</h2>
    <div class="row">
      <div class="img photo" role="img" aria-label="Photo of a business team joining hands"></div>
      <div class="lists">
        <div><h4>Investors</h4><ul><li>Venture Capital</li><li>Angel Investors</li><li>Private Equity</li></ul></div>
        <div><h4>Other Sources</h4><ul><li>Research Grants</li><li>University Funds</li><li>Strategic Partners</li><li>Bank Loans</li></ul></div>
      </div>
    </div>
  </section>

  <footer class="foot">
    <div class="subscribe"><h4>Subscribe to Our News</h4><div class="field"><span>Enter your email address</span><b>Subscribe</b></div></div>
    <div class="links">
      <div class="col"><div class="logo">The K7 Momentum Collective</div><p>Helping science teams build fundable life science companies.</p></div>
      <div class="col"><h4>Quick Links</h4><ul><li>About Us</li><li>The Solution</li><li>Funding</li></ul></div>
      <div class="col"><h4>Services</h4><ul><li>Market Case</li><li>Product Blueprint</li><li>CEO Report</li></ul></div>
      <div class="col"><h4>Contact</h4><ul><li>(555) 014-2280</li><li>hello@k7momentum.example</li></ul></div>
    </div>
    <div class="copy">© The K7 Momentum Collective. All rights reserved.</div>
  </footer>
</div>

<!-- ===== Version 2 ===== -->
<div class="page v2">
  <header class="hero">
    <div class="topbar"><span class="logo">The K7 Momentum Collective</span><span class="phone">(555) 014-2280</span></div>
    <nav class="menu"><span>Home</span><span>About Us</span><span>The Solution</span><span>Product Definition</span><span>Plan Elements</span><span>Funding</span><span>Contact</span></nav>
    <div class="hero-copy">
      <h1>The K7 Momentum Collective</h1>
      <p>Accelerating new life science ventures from discovery to market.</p>
      <span class="btn" style="background:#fff;color:var(--violet)">Learn More</span>
    </div>
    <div class="hero-art" role="img" aria-label="Illustration of growth charts on a large digital screen"></div>
  </header>

  <section class="about">
    <div class="txt">
      <span class="label">About Us</span>
      <h2>The K7 Momentum Collective</h2>
      <p class="p">The K7 Momentum Collective guides academic inventors and early investors through a structured path that turns promising research in diagnostics and medical devices into a fundable company.</p>
      <span class="btn">Read More</span>
    </div>
    <div class="img photo hex" role="img" aria-label="Photo of a business professional in a suit"></div>
  </section>

  <section class="solution">
    <div class="img photo hex" role="img" aria-label="Photo of colleagues meeting around a table"></div>
    <div class="txt">
      <span class="label">What We Offer</span>
      <h2>The Solution</h2>
      <p class="p">A proven framework that reduces risk and shortens the time to a credible investment case.</p>
      <ul class="ticks">
        <li>Define the market and the clinical need</li>
        <li>Shape the product that wins the market</li>
        <li>Build the blueprint for development and launch</li>
        <li>Present a clear plan to investors and boards</li>
      </ul>
    </div>
  </section>

  <section class="discovery">
    <h2 class="sec-title">Discovery to Market</h2>
    <svg width="480" height="110" viewBox="0 0 480 110" aria-label="Five stage process from discovery to market">
      <g fill="none" stroke="#5b2ee8" stroke-width="2">
        <circle cx="48" cy="55" r="38"/><circle cx="144" cy="55" r="38"/><circle cx="240" cy="55" r="38"/><circle cx="336" cy="55" r="38"/><circle cx="432" cy="55" r="38"/>
      </g>
      <g stroke="#3a2bd0" stroke-width="1.5" fill="#3a2bd0">
        <line x1="86" y1="55" x2="104" y2="55"/><path d="M104 51 L110 55 L104 59Z"/>
        <line x1="182" y1="55" x2="200" y2="55"/><path d="M200 51 L206 55 L200 59Z"/>
        <line x1="278" y1="55" x2="296" y2="55"/><path d="M296 51 L302 55 L296 59Z"/>
        <line x1="374" y1="55" x2="392" y2="55"/><path d="M392 51 L398 55 L392 59Z"/>
      </g>
      <g font-family="Poppins,Arial,sans-serif" font-size="8" font-weight="600" fill="#1d2433" text-anchor="middle">
        <text x="48" y="58">Discovery</text>
        <text x="144" y="54">Market</text><text x="144" y="64">Case</text>
        <text x="240" y="54">Winning</text><text x="240" y="64">Product</text>
        <text x="336" y="54">Product</text><text x="336" y="64">Blueprint</text>
        <text x="432" y="54">Launch &amp;</text><text x="432" y="64">Funding</text>
      </g>
    </svg>
  </section>

  <section class="product">
    <span class="label center">Our Process</span>
    <h2 class="sec-title">Product Definition</h2>
    <div class="phase">
      <div class="txt"><span class="label">Phase 1</span><h3>The Market Case (30 – 45 days)</h3>
        <p class="p">We size the opportunity, map the competition and confirm the unmet clinical need. Interviews with clinicians, payers and buyers show who will pay and why the product matters.</p></div>
      <div class="img photo hex" role="img" aria-label="Photo of a city skyline with rising bar chart overlay"></div>
    </div>
    <div class="phase flip">
      <div class="txt"><span class="label">Phase 2</span><h3>The Winning Product (30 – 45 days)</h3>
        <p class="p">We turn market insight into product requirements, pricing and positioning, so the team builds what customers will adopt and investors will back.</p></div>
      <div class="img photo hex" role="img" aria-label="Photo of a professional pointing at a digital screen"></div>
    </div>
    <div class="phase band">
      <div class="txt"><span class="label">Phase 3</span><h3>The Product Blueprint (45 – 60 days)</h3>
        <p class="p">A development roadmap with regulatory path, milestones, budget and team plan that carries the product from prototype to first sales.</p></div>
      <div class="img photo hex" role="img" aria-label="Photo of a team reviewing plans at a desk"></div>
    </div>
    <div class="phase flip">
      <div class="txt"><span class="label">Phase 4</span><h3>CEO Report out (15 days)</h3>
        <div class="cols"><span>Market summary</span><span>Product profile</span><span>Regulatory path</span><span>Funding needs</span><span>Key milestones</span><span>Risk review</span></div></div>
      <div class="img photo hex" role="img" aria-label="Photo of hands shaking over a business desk"></div>
    </div>
  </section>

  <section class="plan">
    <h2 class="sec-title">K7 Plan Elements</h2>
    <div class="grid">
      <div class="card"><svg class="ico" width="26" height="26"><circle cx="13" cy="13" r="11" fill="none" stroke="#5b2ee8" stroke-width="2"/></svg><h4>Executive Summary</h4><p class="p">A short view of the need, the product and the ask.</p></div>
      <div class="card on"><svg class="ico" width="26" height="26"><circle cx="13" cy="13" r="11" fill="none" stroke="#fff" stroke-width="2"/></svg><h4>Company Description</h4><p class="p">Mission, team, structure and the science behind it.</p></div>
      <div class="card"><svg class="ico" width="26" height="26"><circle cx="13" cy="13" r="11" fill="none" stroke="#5b2ee8" stroke-width="2"/></svg><h4>Products/Services</h4><p class="p">What we sell, who uses it and how it is priced.</p></div>
      <div class="card"><svg class="ico" width="26" height="26"><circle cx="13" cy="13" r="11" fill="none" stroke="#5b2ee8" stroke-width="2"/></svg><h4>Market Analysis</h4><p class="p">Size, segments, trends and the competitive field.</p></div>
      <div class="card"><svg class="ico" width="26" height="26"><circle cx="13" cy="13" r="11" fill="none" stroke="#5b2ee8" stroke-width="2"/></svg><h4>Operational Strategy</h4><p class="p">Development, quality, supply and go to market.</p></div>
      <div class="card"><svg class="ico" width="26" height="26"><circle cx="13" cy="13" r="11" fill="none" stroke="#5b2ee8" stroke-width="2"/></svg><h4>Financials</h4><p class="p">Forecasts, budget and the use of funds raised.</p></div>
    </div>
  </section>

  <section class="areas">
    <div class="txt">
      <span class="label">What We Cover</span>
      <h2>Key areas Covered</h2>
      <div class="table">
        <div><b>Clinical need</b> and use</div><div><b>Pricing</b> model</div>
        <div><b>Market size</b> and growth</div><div><b>Reimbursement</b> path</div>
        <div><b>Competition</b> review</div><div><b>Regulatory</b> plan</div>
        <div><b>Customer</b> interviews</div><div><b>IP</b> position</div>
        <div><b>Product</b> requirements</div><div><b>Team</b> and hiring</div>
        <div><b>Positioning</b> and message</div><div><b>Funding</b> strategy</div>
      </div>
    </div>
    <div class="img photo" role="img" aria-label="Photo of a smiling businessman in a suit"></div>
  </section>

  <section class="funding">
    <h2 class="sec-title">Funding</h2>
    <div class="row">
      <div class="img photo" role="img" aria-label="Photo of a business team joining hands"></div>
      <div class="lists">
        <div><h4>Investors</h4><ul><li>Venture Capital</li><li>Angel Investors</li><li>Private Equity</li></ul></div>
        <div><h4>Other Sources</h4><ul><li>Research Grants</li><li>University Funds</li><li>Strategic Partners</li><li>Bank Loans</li></ul></div>
      </div>
    </div>
  </section>

  <footer class="foot">
    <div class="links">
      <div class="col"><div class="logo">The K7 Momentum Collective</div><p>Helping science teams build fundable life science companies.</p></div>
      <div class="col"><h4>Quick Links</h4><ul><li>About Us</li><li>The Solution</li><li>Funding</li></ul></div>
      <div class="col"><h4>Services</h4><ul><li>Market Case</li><li>Product Blueprint</li><li>CEO Report</li></ul></div>
      <div class="col"><h4>Contact</h4><ul><li>(555) 014-2280</li><li>hello@k7momentum.example</li></ul></div>
    </div>
    <div class="copy" style="color:#e0d7ff">© The K7 Momentum Collective. All rights reserved.</div>
  </footer>
</div>

</body>
</html>
```